Business Card Design for my Real Estate Investing Company

This is for a Real Estate Investing Company that will be serving the Las Vegas Valley. Id like the following slogan included: "Investing in Our Community" I have attached my logo. You will see the color tones I'm interested in..in my logo. I would like the card to be double-sided with a modern, professional look.
Target Market(s)
Homeowners, banks, real estate industry
Industry/Entity Type
Real Estate
Contact Information for Business Card
name: Dale Marwick
position: Managing Member
address: 4182 Corvello Pkwy ste 317-200
N. Las Vegas, NV 89117
phone: (702) 555-0143
fax: (702) 555-0187
email: SunridgeCrestPropertyGroup@mailbox-example.com
web: SunridgeCrestPropertyGroups.com
*At the bottom of the card I would like....
We buy houses for cash....no repairs, no commissions, no fees!
Logo Text
SUNRIDGE CREST PROPERTY GROUP "Investing in Our Community"
Font styles to use
Other font styles liked:
- Lora
Requirements
Must have
- On the back of the card, i'd like to have my logo large and the following statements:
- Are you considering selling your home? Want a simple, hassle-free transaction? We can help! We buy houses for cash and can close quickly! No need to do any repairs, no realtor commissions, no closing costs.....and no headaches. Let us help you with your real estate needs...!
Nice to have
- multiple colors 2 two tone on front and back

```html
<!DOCTYPE html>
<html lang="en">
<head>
<meta charset="utf-8">
<title>Sunridge Crest Property Group – Business Card</title>
<link rel="stylesheet" href="https://fonts.googleapis.com/css2?family=Lora:ital,wght@0,400;0,700;1,400;1,700&family=Raleway:wght@400;500&display=swap">
<style>
  :root {
    --page-bg: #e9e7e4;
    --brand-blue: #1f5fb4;
    --brand-blue-deep: #0d3f8f;
    --brand-blue-light: #3d8fd6;
    --ink-gray: #5c5f66;
    --rule-gray: #c9ccd1;
    --stripe-gray: #b9bcc1;
    --card-white: #ffffff;
  }
  * { box-sizing: border-box; margin: 0; padding: 0; }
  html, body { width: 1200px; height: 900px; overflow: hidden; }
  body { background: var(--page-bg); position: relative; font-family: "Raleway", sans-serif; }

  .card {
    position: absolute;
    width: 600px;
    height: 343px;
    border-radius: 4px;
    box-shadow: 0 6px 18px rgba(0,0,0,.18);
    overflow: hidden;
  }

  /* Shared brand block */
  .brand-name {
    font-family: "Lora", serif;
    font-weight: 700;
    letter-spacing: .5px;
    line-height: 1.15;
    display: flex; align-items: center; justify-content: center;
  }
  .brand-mark { background: currentColor; flex: none; }
  .brand-words { display: block; text-align: left; }
  .brand-slogan { font-family: "Lora", serif; letter-spacing: 2px; }

  /* Back side */
  .card-back {
    left: 60px; top: 70px;
    background: linear-gradient(160deg, var(--brand-blue-light) 0%, var(--brand-blue) 50%, var(--brand-blue-deep) 100%);
    color: #fff;
    text-align: center;
    padding: 32px 40px 0;
  }
  .back-pitch {
    font-family: "Lora", serif;
    font-size: 15px;
    line-height: 1.42;
  }
  .back-brand { margin-top: 24px; }
  .card-back .brand-name { font-size: 28px; gap: 14px; }
  .card-back .brand-mark { width: 22px; height: 22px; }
  .card-back .brand-slogan { font-size: 15px; margin-top: 8px; }

  /* Front side */
  .card-front {
    left: 540px; top: 487px;
    background: var(--card-white);
  }
  .front-brand {
    position: absolute; left: 16px; top: 118px; width: 270px;
    color: var(--brand-blue); text-align: center;
  }
  .card-front .brand-name { font-size: 19px; gap: 10px; }
  .card-front .brand-mark { width: 14px; height: 14px; }
  .card-front .brand-slogan { font-size: 10px; margin-top: 6px; color: var(--ink-gray); letter-spacing: 1.5px; }

  .front-divider {
    position: absolute; left: 300px; top: 0; width: 1px; height: 238px;
    background: var(--rule-gray);
  }
  .contact {
    position: absolute; left: 314px; top: 40px; right: 12px;
    color: var(--ink-gray); font-size: 11px; line-height: 1.6;
  }
  .contact-name { color: var(--brand-blue); font-size: 17px; letter-spacing: 1px; font-weight: 500; line-height: 1.2; }
  .contact-role { font-size: 12px; margin-bottom: 22px; }
  .contact-line { display: flex; align-items: center; gap: 6px; white-space: nowrap; }
  .contact-line svg { width: 11px; height: 11px; flex: none; fill: var(--brand-blue); }
  .contact-email { font-size: 9px; letter-spacing: -.1px; }

  .web-band {
    position: absolute; right: 0; top: 238px; width: 300px; height: 26px;
    background: var(--brand-blue);
    clip-path: polygon(8% 0, 100% 0, 100% 100%, 0 100%);
    color: #fff; font-size: 11px;
    display: flex; align-items: center; justify-content: flex-end; gap: 6px; padding-right: 14px;
  }
  .web-band svg { width: 11px; height: 11px; fill: none; stroke: #fff; stroke-width: 1.6; }
  .front-tagline {
    position: absolute; left: 28px; top: 276px;
    font-family: "Lora", serif; font-style: italic; font-weight: 700;
    color: var(--brand-blue); font-size: 16.5px; white-space: nowrap;
  }
  .gray-stripe {
    position: absolute; left: 0; bottom: 0; width: 600px; height: 22px;
    background: linear-gradient(90deg, var(--stripe-gray), #e3e5e8 70%, #fff);
  }
</style>
</head>
<body>

<section class="card card-back" aria-label="Card back">
  <p class="back-pitch">
    Are you considering selling your home?<br>
    Want a simple, hassle-free transaction?<br>
    We can help! We buy houses for cash and can close quickly!<br>
    No need to do any repairs, no realtor commissions,<br>
    no closing costs.....and no headaches.<br>
    Let us help you with your real estate needs...!
  </p>
  <div class="back-brand">
    <div class="brand-name"><span class="brand-mark"></span><span class="brand-words">SUNRIDGE CREST<br>PROPERTY GROUP</span></div>
    <div class="brand-slogan">“Investing in Our Community”</div>
  </div>
</section>

<section class="card card-front" aria-label="Card front">
  <div class="front-brand">
    <div class="brand-name"><span class="brand-mark"></span><span class="brand-words">SUNRIDGE CREST<br>PROPERTY GROUP</span></div>
    <div class="brand-slogan">“Investing in Our Community”</div>
  </div>

  <div class="front-divider"></div>

  <div class="contact">
    <div class="contact-name">DALE MARWICK</div>
    <div class="contact-role">Managing Member</div>
    <div class="contact-line">4182 Corvello Pkwy ste 317-200</div>
    <div class="contact-line">N. Las Vegas, NV 89117</div>
    <div class="contact-line">
      <svg viewBox="0 0 24 24"><path d="M6.6 10.8a15 15 0 0 0 6.6 6.6l2.2-2.2a1 1 0 0 1 1-.25 11.4 11.4 0 0 0 3.6.57 1 1 0 0 1 1 1V20a1 1 0 0 1-1 1A17 17 0 0 1 3 4a1 1 0 0 1 1-1h3.5a1 1 0 0 1 1 1c0 1.25.2 2.45.57 3.57a1 1 0 0 1-.25 1z"/></svg>
      (702) 555-0143
    </div>
    <div class="contact-line">
      <svg viewBox="0 0 24 24"><path d="M6 3h10v5H6zM4 9h16a2 2 0 0 1 2 2v6h-4v4H6v-4H2v-6a2 2 0 0 1 2-2zm4 7v3h8v-3z"/></svg>
      (702) 555-0187
    </div>
    <div class="contact-line contact-email">
      <svg viewBox="0 0 24 24"><path d="M2 11 22 3l-7 19-3-8z"/></svg>
      SunridgeCrestPropertyGroup@mailbox-example.com
    </div>
  </div>

  <div class="web-band">
    <svg viewBox="0 0 24 24"><circle cx="12" cy="12" r="9"/><path d="M3 12h18M12 3c3 3 3 15 0 18M12 3c-3 3-3 15 0 18"/></svg>
    www.SunridgeCrestPropertyGroups.com
  </div>

  <p class="front-tagline">We buy houses for cash....no repairs, no commissions, no fees!</p>
  <div class="gray-stripe"></div>
</section>

</body>
</html>
```